Building company buisness cards

We are looking for a sharp modern new look for our business cards.
We are a New Zealand based company that specialises in house and land packages.
We have attached a photo of the current logo and would like to see if it can be improved somehow if needed.
We are open to any colours but we have chosen green at this stage.
Feel free to change the font and make the logo smarter looking.
Play with the colours and see what looks best.

We want a card that looks so good know one will want to throw it away!

Target Market(s)

Home buyers

Industry/Entity Type

Building

Contact Information for Business Card

Dorian Keswick
0217392604
dkeswick@tidewellhomecraft.co.nz
tidewellhomecraft.co.nz

Font styles to use
Serif
Sans Serif

Colors

Designer to choose colors to be used in the design.

Requirements
Must have
• Logo and company name on one side, details on the other side
Nice to have
• Color codes for the original green are HEX #4a8028, RGB(74,128,40), CMYK(42,0,69,50)
• Round corners, Raised and/or spot UV

```html
<!DOCTYPE html>
<html lang="en">
<head>
<meta charset="utf-8">
<title>Tidewell Homecraft – Business Card</title>
<link rel="stylesheet" href="https://fonts.googleapis.com/css2?family=Montserrat:wght@500;600&family=Open+Sans:wght@400&display=swap">
<style>
  :root{
    --green:#52b848;
    --charcoal:#2b2a2b;
    --ink:#1e1e1e;
    --white:#ffffff;
    --stage:#ececec;
  }
  *{margin:0;padding:0;box-sizing:border-box}
  html,body{width:1200px;height:1200px;overflow:hidden;background:var(--stage)}
  .canvas{position:relative;width:1200px;height:1200px}
  .card{position:absolute;left:240px;width:720px;height:480px;overflow:hidden}
  .card--front{top:70px;background:var(--charcoal)}
  .card--back{top:610px;background:var(--white);outline:1px solid #9a9a9a}
  .card__shapes{position:absolute;inset:0;width:720px;height:480px}

  .company-name{position:absolute;left:0;width:100%;
    display:flex;align-items:center;justify-content:center;
    font-family:"Montserrat",sans-serif;font-weight:600;line-height:1;white-space:nowrap}
  .company-name__square{flex:none;background:var(--green)}
  .card--front .company-name{top:218px;height:44px;font-size:36px;color:var(--white)}
  .card--front .company-name__square{width:22px;height:22px;margin-right:16px}
  .card--back .company-name{top:78px;height:32px;font-size:24px;color:var(--ink)}
  .card--back .company-name__square{width:15px;height:15px;margin-right:11px;background:var(--white)}

  .person-name{position:absolute;top:175px;left:0;width:100%;height:65px;
    display:flex;align-items:center;justify-content:center;
    font-family:"Montserrat",sans-serif;font-weight:500;font-size:31px;
    letter-spacing:4px;color:var(--white)}

  .contact-list{position:absolute;left:96px;top:305px;list-style:none}
  .contact-list__item{display:flex;align-items:center;height:52px}
  .contact-list__icon{width:38px;height:42px;flex:none}
  .contact-list__text{margin-left:30px;font-family:"Open Sans",sans-serif;
    font-size:21px;color:var(--green)}
</style>
</head>
<body>
<main class="canvas">

  <section class="card card--front" aria-label="Card front">
    <svg class="card__shapes" viewBox="0 0 720 480" aria-hidden="true">
      <polygon fill="var(--green)" points="0,77 60,113 60,368 0,403"/>
      <polygon fill="var(--green)" points="720,77 660,113 660,368 720,403"/>
    </svg>
    <div class="company-name">
      <span class="company-name__square" aria-hidden="true"></span>
      <span class="company-name__text">Tidewell Homecraft</span>
    </div>
  </section>

  <section class="card card--back" aria-label="Card back">
    <svg class="card__shapes" viewBox="0 0 720 480" aria-hidden="true">
      <rect fill="var(--green)" x="0" y="0" width="720" height="197"/>
      <polygon fill="#111" points="78,197 108,175 130,197"/>
      <polygon fill="#111" points="642,197 612,175 590,197"/>
      <polygon fill="var(--charcoal)" points="108,175 612,175 570,240 150,240"/>
    </svg>
    <div class="company-name">
      <span class="company-name__square" aria-hidden="true"></span>
      <span class="company-name__text">Tidewell Homecraft</span>
    </div>
    <div class="person-name">Dorian Keswick</div>

    <ul class="contact-list">
      <li class="contact-list__item">
        <svg class="contact-list__icon" viewBox="0 0 38 42" aria-label="Phone">
          <polygon fill="var(--green)" points="19,0 38,10.5 38,31.5 19,42 0,31.5 0,10.5"/>
          <path fill="var(--white)" d="M10 17c0-3 4-5 9-5s9 2 9 5l-3 1.5-2-2.5h-8l-2 2.5zM12 20h14l2 9H10z"/>
          <circle cx="19" cy="24.5" r="2.5" fill="var(--green)"/>
        </svg>
        <span class="contact-list__text">0217392604</span>
      </li>
      <li class="contact-list__item">
        <svg class="contact-list__icon" viewBox="0 0 38 42" aria-label="Email">
          <polygon fill="var(--green)" points="19,0 38,10.5 38,31.5 19,42 0,31.5 0,10.5"/>
          <g fill="none" stroke="var(--white)" stroke-width="1.8">
            <circle cx="19" cy="21" r="9"/>
            <ellipse cx="19" cy="21" rx="4" ry="9"/>
            <line x1="10" y1="21" x2="28" y2="21"/>
            <line x1="12" y1="16" x2="26" y2="16"/>
            <line x1="12" y1="26" x2="26" y2="26"/>
          </g>
        </svg>
        <span class="contact-list__text">dkeswick@tidewellhomecraft.co.nz</span>
      </li>
      <li class="contact-list__item">
        <svg class="contact-list__icon" viewBox="0 0 38 42" aria-label="Website">
          <polygon fill="var(--green)" points="19,0 38,10.5 38,31.5 19,42 0,31.5 0,10.5"/>
          <g fill="none" stroke="var(--white)" stroke-width="1.8">
            <rect x="9.5" y="14" width="19" height="14"/>
            <polyline points="9.5,14 19,22 28.5,14"/>
          </g>
        </svg>
        <span class="contact-list__text">tidewellhomecraft.co.nz</span>
      </li>
    </ul>
  </section>

</main>
</body>
</html>
```